Design Brief for Website Redesign

Client Name: Velmora IT
Website: www.velmorait.com.au
Industry: Managed IT Services
Target Audience: Small to medium-sized businesses in Australia, requiring IT solutions, IT support, cloud services, and phone systems.

Project Overview
We are seeking a full redesign of the Velmora IT website to modernize its look, improve usability, and enhance user experience across devices. The goal is to create a professional, clean, and user-friendly website that reflects our expertise in IT services and appeals to our business clients.

Objectives
Modern Visual Identity: Create a fresh, modern design that aligns with Velmora IT's branding.

Improved User Experience: Simplify navigation, improve accessibility, and enhance mobile responsiveness.

Clear Calls to Action: Ensure CTAs are prominent and encourage user engagement.

Enhanced Trust & Credibility: Highlight testimonials, case studies, and industry credentials.

SEO Optimization: Ensure the site is optimized for search engines, including proper heading structures and metadata.
Design Style & Tone
Professional: Clean, modern, and polished to reflect our IT expertise.

Minimalist: Simple layouts, plenty of white space, and easy-to-read typography.

Tech-focused: Subtle tech-themed design elements that reinforce our brand as a leading IT service provider.

Colors: Use our existing brand colors, or propose a color scheme that complements the tech industry while maintaining a professional feel.

Typography: Clear, readable fonts that convey professionalism and trustworthiness.

Key Pages & Features
Home Page:

Hero section with a clear value proposition.

Highlight key services (IT support, cloud solutions, phone systems, etc.) with icons and brief descriptions.

Prominent CTAs (e.g., “Request a Quote,” “Book a Demo”).

Testimonials from satisfied clients.

Services Page:

Detailed breakdown of the services we offer (IT support, cloud services, phone systems, etc.).

Use of icons or illustrations to make the services visually engaging.

Clear CTAs to request quotes or book consultations.

About Us Page:

Information about our company history, mission, and team.

Highlight our certifications, partnerships, and industry expertise.

Case Studies/Testimonials Page:

Showcase client success stories and testimonials with visuals and brief case study summaries.

Include a trust-building section with logos of major clients or partners.

Contact Page:

Simple contact form for inquiries.

Integrated map with office location.

Social media links and phone number.

Blog/Resource Section:

Easy-to-navigate blog section for IT-related articles, tips, and industry news.

Clear categorization and tags for easy browsing.

Knowledge Base/Support Page:

Self-service area for clients to find articles, FAQs, and support guides.

Option to submit a support ticket.

Mobile Responsiveness:

Ensure the design is fully responsive, with no horizontal scrolling or misaligned content on mobile.

Functional Requirements
Fast Load Times: Optimize images, minimize unnecessary scripts, and ensure the site loads quickly on both desktop and mobile.

User-Friendly CMS: We need a CMS that is easy to update (preferably WordPress, but open to other suggestions).

SEO Best Practices: Structure the site with proper metadata, alt tags, and semantic HTML for better search engine optimization.

Security: Ensure the website follows security best practices (SSL, HTTPS).

Deliverables
Full website design (desktop and mobile versions).

Design mockups in Photoshop, Sketch, or Figma (whichever is preferred).

Working prototype (optional).

Final website files, including images and assets.

A style guide for ongoing consistency.

Industry/Entity Type

IT Managed Services

Number of Pages Required

3 page

Requirements
Must have
• EXCELLENT UX/UI

```html
<!DOCTYPE html>
<html lang="en">
<head>
<meta charset="utf-8">
<title>Velmora IT – Technology Solutions for a better business</title>
<link href="https://fonts.googleapis.com/css2?family=Open+Sans:wght@400;500;600;700&family=Noto+Serif:wght@400&display=swap" rel="stylesheet">
<style>
:root{
  --red:#e31b3a;
  --ink:#111111;
  --text:#333333;
  --muted:#5c5c5c;
  --card:#f3f3f3;
  --band:#f1f1f1;
  --line:#d6d6d6;
  --white:#ffffff;
  --hero-a:#1a0b2b;
  --hero-b:#2c2f5a;
  --hero-c:#4b6a8a;
}
*{box-sizing:border-box;margin:0;padding:0}
html,body{width:1200px;height:2592px;overflow:hidden}
body{font-family:"Open Sans",Arial,sans-serif;color:var(--text);background:var(--white);position:relative}
a{color:inherit;text-decoration:none}
.abs{position:absolute}

/* header */
.site-header{position:absolute;left:0;top:0;width:1200px;height:94px;background:var(--white);border-top:2px solid var(--red)}
.brand{position:absolute;left:111px;top:20px;font-size:44px;font-weight:700;color:var(--red);letter-spacing:-1px;line-height:1}
.topbar{position:absolute;left:460px;top:0;width:740px;height:42px;background:var(--red);clip-path:polygon(0 0,100% 0,100% 100%,24px 100%);color:var(--white);font-size:15px}
.topbar span{position:absolute;top:11px;display:flex;align-items:center;gap:7px}
.topbar b{font-weight:700}
.topbar .social{display:flex;gap:12px}
.topbar .social i{display:block;width:12px;height:12px;border-radius:50%;background:var(--white)}
.main-nav{position:absolute;top:57px;left:465px;display:flex;gap:44px;font-size:16px;color:var(--ink)}
.main-nav .active{color:var(--red)}

/* hero */
.hero{position:absolute;left:0;top:94px;width:1200px;height:581px;background:linear-gradient(120deg,var(--hero-a) 0%,#241539 35%,var(--hero-b) 65%,var(--hero-c) 100%);overflow:hidden}
.hero-visual{position:absolute;left:560px;top:80px;width:600px;height:500px;background:radial-gradient(ellipse at 45% 45%,#3d6fb0 0%,#23406e 35%,rgba(40,50,90,0) 70%)}
.hero h1{position:absolute;left:111px;top:148px;width:520px;font-size:46px;line-height:59px;font-weight:600;color:var(--white)}
.hero p{position:absolute;left:111px;top:270px;width:470px;font-size:15px;line-height:31px;color:var(--white)}
.btn{display:inline-flex;align-items:center;justify-content:center;font-weight:600;font-size:16px}
.btn-red{background:var(--red);color:var(--white)}
.btn-white{background:var(--white);color:var(--red)}
.hero .btn{position:absolute;top:386px;height:48px}
.scroll-cue{position:absolute;left:558px;top:654px;width:84px;height:84px;border-radius:50%;background:var(--white)}
.scroll-cue span{position:absolute;left:31px;top:16px;width:22px;height:36px;border-radius:11px;background:#8a8a8a}

/* headings */
.section-title{position:absolute;left:0;width:1200px;text-align:center;font-size:36px;font-weight:400;color:var(--ink)}
.section-title b{font-weight:700}
.section-title::after{content:"";display:block;width:68px;height:3px;background:var(--red);margin:16px auto 0}

/* services */
.service{position:absolute;top:877px;background:var(--card);border-top:3px solid var(--ink);text-align:center}
.service .icon{width:76px;height:76px;border-radius:50%;background:#dcdcdc;margin:30px auto 0;display:flex;align-items:center;justify-content:center}
.service h3{font-size:21px;font-weight:600;color:var(--ink);margin-top:22px}
.service p{font-size:14.5px;line-height:26px;color:#222;margin:12px 10px 0}
.service .more{display:inline-block;margin-top:12px;font-size:15px;font-weight:600;text-decoration:underline;color:var(--ink)}
.service.featured{background:var(--white);border-top-color:var(--red);box-shadow:0 4px 14px rgba(0,0,0,.18)}
.featured .photo{width:308px;height:193px;margin:19px auto 0;background:linear-gradient(135deg,#0b2a6a,#1a4fb5 50%,#0a1f55)}
.featured .badge{width:76px;height:76px;border-radius:50%;background:var(--red);border:4px solid var(--white);margin:-38px auto 0;position:relative;display:flex;align-items:center;justify-content:center}
.featured h3{color:var(--red);margin-top:8px}
.featured .more{color:var(--red);text-decoration:underline}
.view-all{position:absolute;left:517px;top:1357px;width:167px;height:48px}

/* testimonials */
.testimonials{position:absolute;left:0;top:1508px;width:1200px;height:560px;background:var(--band)}
.quote-card{position:absolute;top:182px;width:434px;height:267px;background:var(--white);border-radius:12px;padding:32px}
.avatar{position:absolute;left:32px;top:20px;width:74px;height:74px;border-radius:50%;background:linear-gradient(160deg,#9a8d86,#4a4a52)}
.qmark{position:absolute;left:88px;top:68px;width:28px;height:28px;border-radius:50%;background:var(--red);border:2px solid var(--white)}
.quote-card h4{position:absolute;left:135px;top:20px;font-size:18px;font-weight:600;color:var(--ink)}
.quote-card .loc{position:absolute;left:135px;top:48px;font-family:"Noto Serif",Georgia,serif;font-size:14px;color:#333}
.quote-card .stars{position:absolute;left:135px;top:72px;display:flex;gap:1px}
.quote-card blockquote{position:absolute;left:32px;top:118px;width:372px;font-size:15px;line-height:26px;color:var(--muted);font-weight:400}
.arrow{position:absolute;top:300px}

/* footer */
.site-footer{position:absolute;left:0;top:2068px;width:1200px;height:524px}
.foot-brand{position:absolute;left:0;width:1200px;top:62px;text-align:center;font-size:82px;font-weight:700;color:var(--red);letter-spacing:-2px;line-height:1}
.foot-nav{position:absolute;left:111px;top:188px;width:978px;height:59px;border-top:1px solid var(--line);border-bottom:1px solid var(--line);display:flex;align-items:center;justify-content:center;gap:38px;font-size:16px;color:var(--ink)}
.contact{position:absolute;top:288px;display:flex;align-items:center;gap:10px;font-size:16px;color:var(--ink)}
.contact b{font-weight:600}
.contact .ring{width:40px;height:40px;border-radius:50%;border:2px solid var(--red);display:flex;align-items:center;justify-content:center}
.social-row{position:absolute;left:111px;top:395px;width:978px;height:1px;background:var(--line)}
.social-row .dots{position:absolute;left:408px;top:-14px;display:flex;gap:15px;background:var(--white);padding:0 8px}
.social-row .dots i{width:28px;height:28px;border-radius:50%;background:var(--red);display:block}
.copyright{position:absolute;left:0;width:1200px;top:442px;text-align:center;font-size:16px;color:var(--ink)}
</style>
</head>
<body>

<header class="site-header">
  <a class="brand" href="#">Velmora</a>
  <div class="topbar">
    <span style="left:92px">
      <svg width="13" height="13" viewBox="0 0 24 24"><path fill="#fff" d="M6.6 10.8a15 15 0 0 0 6.6 6.6l2.2-2.2c.3-.3.7-.4 1-.2 1.1.4 2.3.6 3.6.6.6 0 1 .4 1 1V20c0 .6-.4 1-1 1A17 17 0 0 1 3 4c0-.6.4-1 1-1h3.5c.6 0 1 .4 1 1 0 1.3.2 2.5.6 3.6.1.3 0 .7-.2 1z"/></svg>
      <b>Phone:</b> 1300 555 014
    </span>
    <span style="left:313px">
      <svg width="11" height="14" viewBox="0 0 24 30"><path fill="#fff" d="M12 0a10 10 0 0 0-10 10c0 7.5 10 20 10 20s10-12.5 10-20A10 10 0 0 0 12 0zm0 14a4 4 0 1 1 0-8 4 4 0 0 1 0 8z"/></svg>
      <b>Address:</b> Sydney, Australia
    </span>
    <span style="left:568px" class="social"><i></i><i></i><i></i></span>
  </div>
  <nav class="main-nav">
    <a class="active" href="#">Home</a>
    <a href="#">About Us</a>
    <a href="#">Services</a>
    <a href="#">Knowledge Base/Support</a>
    <a href="#">Contact Us</a>
  </nav>
</header>

<section class="hero">
  <div class="hero-visual" role="img" aria-label="Laptop with a glowing cloud and data transfer arrows surrounded by floating folder icons"></div>
  <h1>Technology Solutions for a better business</h1>
  <p>We understand that technology is a critical component of running a successful business, and that's why we're here to help you navigate the ever-changing landscape of IT.</p>
  <a class="btn btn-red" href="#" style="left:111px;width:155px">Request a Quote</a>
  <a class="btn btn-white" href="#" style="left:279px;width:141px">Book a Demo</a>
</section>
<div class="scroll-cue"><span></span>
  <svg class="abs" style="left:36px;top:22px" width="12" height="24" viewBox="0 0 12 24"><path d="M6 2v19M1 16l5 5 5-5" stroke="#fff" stroke-width="1.6" fill="none"/></svg>
</div>

<h2 class="section-title" style="top:772px">Our <b>Services</b></h2>

<article class="service" style="left:111px;width:284px;height:333px">
  <div class="icon">
    <svg width="40" height="38" viewBox="0 0 40 38" fill="none" stroke="#222" stroke-width="1.6"><rect x="2" y="2" width="36" height="24" rx="2"/><path d="M16 26v6M24 26v6M10 34h20"/><circle cx="15" cy="14" r="5"/><path d="M24 10h10M24 14h8M24 18h10"/></svg>
  </div>
  <h3>IT support</h3>
  <p>Equipping your business to work optimally with reliable and optimal managed services. Velmora IT will partner with you to select the best business .</p>
  <a class="more" href="#">Read More</a>
</article>

<article class="service featured" style="left:427px;width:345px;height:443px">
  <div class="photo" role="img" aria-label="Glowing cloud computing chip on a blue circuit board"></div>
  <div class="badge">
    <svg width="40" height="36" viewBox="0 0 40 36" fill="none" stroke="#fff" stroke-width="1.8"><path d="M10 18a7 7 0 0 1 2-13 9 9 0 0 1 17 2 6 6 0 0 1 1 11"/><rect x="8" y="19" width="16" height="5"/><rect x="8" y="25" width="16" height="5"/><rect x="26" y="22" width="8" height="10"/></svg>
  </div>
  <h3>Cloud Solutions</h3>
  <p>We offer a large spectrum of technology solutions, including cloud-based disaster recovery,</p>
  <a class="more" href="#">Read More</a>
</article>

<article class="service" style="left:804px;width:285px;height:333px">
  <div class="icon">
    <svg width="34" height="40" viewBox="0 0 34 40" fill="none" stroke="#222" stroke-width="1.6"><rect x="6" y="2" width="22" height="36" rx="3"/><path d="M13 6h8"/><circle cx="15" cy="20" r="5"/><path d="M19 24l6 7"/></svg>
  </div>
  <h3>Phone Systems</h3>
  <p>Whether it’s a basic landing page or a major app project we can help you showcase your business in the best possible way.</p>
  <a class="more" href="#">Read More</a>
</article>

<a class="btn btn-red view-all" href="#">View all Services</a>

<section class="testimonials">
  <h2 class="section-title" style="top:86px">Client <b>Testimonials</b></h2>

  <svg class="arrow" style="left:78px" width="26" height="44" viewBox="0 0 26 44"><path d="M23 2 3 22l20 20" stroke="#111" stroke-width="2" fill="none"/></svg>

  <article class="quote-card" style="left:149px">
    <div class="avatar" role="img" aria-label="Portrait photo of the client"></div>
    <div class="qmark"></div>
    <h4>Mara Ellison</h4>
    <div class="loc">United State</div>
    <div class="stars">
      <svg width="74" height="14" viewBox="0 0 74 14"><g fill="#f5b400"><path id="st" d="M7 0l2 4.6 5 .4-3.8 3.3 1.2 5L7 10.6 2.6 13.3l1.2-5L0 5l5-.4z"/><use href="#st" x="15"/><use href="#st" x="30"/><use href="#st" x="45"/><use href="#st" x="60"/></g></svg>
    </div>
    <blockquote>Lorem ipsum dolor sit amet, consectetur adipiscing elit, sed do eiusmod tempor incididunt ut labore et dolore magna aliqua. Ut enim ad minim veniam, quis nostrud exercitation ullamco laboris nisi ut aliquip ex ea commodo consequat.</blockquote>
  </article>

  <article class="quote-card" style="left:618px">
    <div class="avatar" role="img" aria-label="Portrait photo of the client"></div>
    <div class="qmark"></div>
    <h4>Daniel Ross</h4>
    <div class="loc">United State</div>
    <div class="stars">
      <svg width="74" height="14" viewBox="0 0 74 14"><g fill="#f5b400"><use href="#st"/><use href="#st" x="15"/><use href="#st" x="30"/><use href="#st" x="45"/><use href="#st" x="60"/></g></svg>
    </div>
    <blockquote>Lorem ipsum dolor sit amet, consectetur adipiscing elit, sed do eiusmod tempor incididunt ut labore et dolore magna aliqua. Ut enim ad minim veniam, quis nostrud exercitation ullamco laboris nisi ut aliquip ex ea commodo consequat.</blockquote>
  </article>

  <svg class="arrow" style="left:1097px" width="26" height="44" viewBox="0 0 26 44"><path d="M3 2l20 20L3 42" stroke="#111" stroke-width="2" fill="none"/></svg>
</section>

<footer class="site-footer">
  <div class="foot-brand">Velmora</div>
  <nav class="foot-nav">
    <a href="#">Home</a><span>|</span>
    <a href="#">About Us</a><span>|</span>
    <a href="#">Knowledge Base/Support</a><span>|</span>
    <a href="#">Services</a><span>|</span>
    <a href="#">Contact Us</a>
  </nav>
  <div class="contact" style="left:186px">
    <span class="ring"><svg width="16" height="16" viewBox="0 0 24 24"><path fill="#e31b3a" d="M6.6 10.8a15 15 0 0 0 6.6 6.6l2.2-2.2c.3-.3.7-.4 1-.2 1.1.4 2.3.6 3.6.6.6 0 1 .4 1 1V20c0 .6-.4 1-1 1A17 17 0 0 1 3 4c0-.6.4-1 1-1h3.5c.6 0 1 .4 1 1 0 1.3.2 2.5.6 3.6.1.3 0 .7-.2 1z"/></svg></span>
    <span><b>Phone:</b> 1300 555 014</span>
  </div>
  <div class="contact" style="left:477px">
    <span class="ring"><svg width="17" height="13" viewBox="0 0 24 18"><rect width="24" height="18" rx="2" fill="#e31b3a"/><path d="M2 3l10 7 10-7" stroke="#fff" stroke-width="2" fill="none"/></svg></span>
    <span><b>Email:</b> info@velmorait.com.au</span>
  </div>
  <div class="contact" style="left:770px">
    <span class="ring"><svg width="13" height="17" viewBox="0 0 24 30"><path fill="#e31b3a" d="M12 0a10 10 0 0 0-10 10c0 7.5 10 20 10 20s10-12.5 10-20A10 10 0 0 0 12 0zm0 14a4 4 0 1 1 0-8 4 4 0 0 1 0 8z"/></svg></span>
    <span><b>Address:</b> Sydney, Australia</span>
  </div>
  <div class="social-row"><div class="dots"><i></i><i></i><i></i><i></i></div></div>
  <p class="copyright">Copyrights@2025.Velmora.All Rights Reserved</p>
</footer>

</body>
</html>
```